Cosmetics Brand Logo and Bottle Label Design

We are creating a new cosmetics brand called "Nolan Whitby" and would like you to create an amazing logo and bottle label for this brand's new 100% pure argan oil product.
For the logo, we really like the logo's of Marin Calloway and Vessa. The text should be Sans Serif (without feet).
For the actual bottle label, please find attached labels of one of our competitors design which really like. We really like the simplicity and elegance of the design. The only difference is that our product will be using light turqoise as the brand color. Please feel free to add your own creativity into it as well.
Industry/Entity Type
Cosmetics
Logo Text
Nolan Whitby
Font styles to use

```html
<!DOCTYPE html>
<html lang="en">
<head>
<meta charset="utf-8">
<title>Nolan Whitby – Argan Oil Identity</title>
<link rel="stylesheet" href="https://fonts.googleapis.com/css2?family=Poiret+One&family=Open+Sans:wght@400&family=Great+Vibes&display=swap">
<style>
  :root {
    --teal: #33b6a0;
    --teal-light: #85d1c6;
    --teal-pale: #c2e9e2;
    --brown: #5e3514;
    --ink: #1c1c1c;
    --paper: #f2ebe7;
    --stripe: rgba(255,255,255,0.45);
  }
  * { margin: 0; padding: 0; box-sizing: border-box; }
  html, body { width: 1200px; height: 1086px; overflow: hidden; }
  body {
    position: relative;
    background: linear-gradient(180deg, #f9f2ed 0%, var(--paper) 100%);
    font-family: "Open Sans", Arial, sans-serif;
  }

  .panel {
    position: absolute;
    left: 14px;
    width: 530px;
    display: flex;
    align-items: center;
    justify-content: center;
  }
  .panel--grey { top: 8px; height: 346px; background: linear-gradient(180deg, #e9e7e6 0%, #bebcbc 100%); }
  .panel--teal { top: 371px; height: 346px; background: linear-gradient(180deg, var(--teal-pale) 0%, #45bba6 100%); }
  .panel--photo { top: 737px; height: 340px; background: radial-gradient(ellipse at 55% 55%, #2a2420 0%, #141210 75%); }

  .lockup { text-align: center; }
  .lockup__name {
    font-family: "Poiret One", "Helvetica Neue", sans-serif;
    font-size: 26px;
    letter-spacing: 0.3em;
    text-transform: uppercase;
    white-space: nowrap;
    padding-left: 0.3em;
  }
  .lockup__rule { height: 1px; width: 150px; margin: 6px auto 5px; }
  .lockup__tagline { font-size: 11px; white-space: nowrap; }

  .lockup--dark  { color: var(--ink); }
  .lockup--dark .lockup__rule { background: #777; }
  .lockup--brown { color: var(--brown); }
  .lockup--brown .lockup__rule { background: var(--brown); opacity: 0.6; }
  .lockup--light { color: #fff; }
  .lockup--light .lockup__rule { background: #bbb; }

  .section-title {
    position: absolute;
    font-family: "Great Vibes", cursive;
    color: var(--brown);
    font-size: 30px;
    line-height: 1;
  }

  .stripes {
    background-color: var(--teal);
    background-image: repeating-linear-gradient(180deg, transparent 0 5px, var(--stripe) 5px 6px);
  }

  .label {
    position: absolute;
    left: 622px; top: 89px;
    width: 493px; height: 275px;
    display: flex;
  }
  .label__side { width: 118px; }
  .label__center {
    flex: 1;
    background: var(--teal);
    display: flex;
    flex-direction: column;
    align-items: center;
    justify-content: flex-end;
    padding-bottom: 10px;
    color: var(--brown);
  }
  .label__center .lockup { margin-bottom: 44px; }
  .label__center .lockup__name { font-size: 16px; }
  .label__center .lockup__rule { width: 100px; margin: 4px auto 3px; }
  .label__center .lockup__tagline { font-size: 7px; }

  .claims { text-align: center; font-size: 10px; line-height: 16px; color: var(--brown); }

  .swatches { position: absolute; left: 634px; top: 381px; display: flex; gap: 6px; }
  .swatch { width: 34px; height: 32px; }
  .swatch--teal { background: var(--teal); }
  .swatch--teal-light { background: var(--teal-light); }
  .swatch--brown { background: var(--brown); }

  .bottle-label {
    position: absolute;
    left: 626px; top: 802px;
    width: 172px; height: 154px;
    display: flex;
  }
  .bottle-label__side { width: 30px; }
  .bottle-label__center {
    flex: 1;
    background: #3fc6b1;
    display: flex;
    flex-direction: column;
    align-items: center;
    justify-content: flex-end;
    padding-bottom: 10px;
  }
  .bottle-label__center .lockup { margin-bottom: 22px; }
  .bottle-label__center .lockup__name { font-size: 8px; letter-spacing: 0.2em; }
  .bottle-label__center .lockup__rule { width: 50px; margin: 2px auto; }
  .bottle-label__center .lockup__tagline { font-size: 4px; }
  .bottle-label__center .claims { font-size: 5px; line-height: 8px; }

  .box {
    position: absolute;
    left: 882px; top: 478px;
    width: 280px; height: 594px;
    background: var(--teal);
    box-shadow: 4px 4px 6px rgba(0,0,0,0.25);
  }
  .box__lockup { position: absolute; left: 0; right: 0; top: 720px; }
  .box .lockup { position: absolute; left: 0; right: 0; top: 238px; }
  .box .lockup__name { font-size: 16px; }
  .box .lockup__rule { width: 100px; margin: 4px auto 3px; }
  .box .lockup__tagline { font-size: 7px; }
  .box .claims { position: absolute; left: 0; right: 0; top: 308px; }
  .box__stripes { position: absolute; left: 0; right: 0; top: 398px; bottom: 0; }
</style>
</head>
<body>

  <section class="panel panel--grey">
    <div class="lockup lockup--dark">
      <div class="lockup__name">Nolan Whitby</div>
      <div class="lockup__rule"></div>
      <div class="lockup__tagline">100% pure argan oil</div>
    </div>
  </section>

  <section class="panel panel--teal">
    <div class="lockup lockup--brown">
      <div class="lockup__name">Nolan Whitby</div>
      <div class="lockup__rule"></div>
      <div class="lockup__tagline">100% pure argan oil</div>
    </div>
  </section>

  <section class="panel panel--photo" role="img" aria-label="Dark still-life photograph of argan oil, nuts and a ceramic tagine behind the logo">
    <div class="lockup lockup--light">
      <div class="lockup__name">Nolan Whitby</div>
      <div class="lockup__rule"></div>
      <div class="lockup__tagline">100% pure argan oil</div>
    </div>
  </section>

  <h2 class="section-title" style="left:640px; top:40px;">label</h2>

  <div class="label">
    <div class="label__side stripes"></div>
    <div class="label__center">
      <div class="lockup lockup--brown">
        <div class="lockup__name">Nolan Whitby</div>
        <div class="lockup__rule"></div>
        <div class="lockup__tagline">100% pure argan oil</div>
      </div>
      <p class="claims">nourishing, moisturizing, revitalizing<br>50ml, 1.7fl oz</p>
    </div>
    <div class="label__side stripes"></div>
  </div>

  <div class="swatches">
    <div class="swatch swatch--teal"></div>
    <div class="swatch swatch--teal-light"></div>
    <div class="swatch swatch--brown"></div>
  </div>

  <h2 class="section-title" style="left:614px; top:436px;">mock up</h2>
  <h2 class="section-title" style="left:896px; top:436px;">box</h2>

  <div class="bottle-label">
    <div class="bottle-label__side stripes"></div>
    <div class="bottle-label__center">
      <div class="lockup lockup--brown">
        <div class="lockup__name">Nolan Whitby</div>
        <div class="lockup__rule"></div>
        <div class="lockup__tagline">100% pure argan oil</div>
      </div>
      <p class="claims">nourishing, moisturizing, revitalizing<br>50ml, 1.7fl oz</p>
    </div>
    <div class="bottle-label__side stripes"></div>
  </div>

  <div class="box">
    <div class="lockup lockup--brown">
      <div class="lockup__name">Nolan Whitby</div>
      <div class="lockup__rule"></div>
      <div class="lockup__tagline">100% pure argan oil</div>
    </div>
    <p class="claims">nourishing, moisturizing, revitalizing<br>50ml, 1.7fl oz</p>
    <div class="box__stripes stripes"></div>
  </div>

</body>
</html>
```